【 概要 】 私が運営しているClipvraチャンネルのサムネイル制作です。 https://www.clipvra-media.example/channel/UCxQ7mTrLbadKwe9RhZ3PkvE?view_as=subscriber 【 依頼内容 】 ・サイズ: 横1,280px × 縦720px ・作成数: 1種類 ・利用用途:Clipvra 【 デザインイメージ 】 ・テキストは白色を主体としてください。 ・背景は切り抜いてもらっても結構です。 【素材】 写真は1点用意しています 【入れていただきたいテキスト】 ◆大キャッチ◆ バンコクへ戻ってまいりました |
インパクトがありつつ、見やすいデザインでしたので採用しました。
たくさんのご提案ありがとうございました。
今後も同様のお仕事を発注してまいりますので、また機会がありましたらよろしくお願いいたします。

```html
<!DOCTYPE html>
<html lang="ja">
<head>
<meta charset="utf-8">
<title>バンコクへ戻ってまいりました</title>
<link rel="stylesheet" href="https://fonts.googleapis.com/css2?family=Noto+Sans+JP:wght@900&display=swap">
<style>
  :root {
    --sky-top: #2f7fd6;
    --sky-low: #8cc3ee;
    --temple-gold: #c8a04a;
    --temple-shade: #6b5431;
    --hoodie: #eceae6;
    --headline-fill: #ffffff;
    --headline-edge: #111111;
  }
  html, body {
    margin: 0;
    padding: 0;
    width: 1200px;
    height: 676px;
    overflow: hidden;
    background: #000;
  }
  .thumbnail {
    position: relative;
    width: 1200px;
    height: 676px;
    overflow: hidden;
  }
  .scene-photo {
    position: absolute;
    inset: 0;
    background:
      radial-gradient(ellipse 190px 300px at 930px 470px, var(--hoodie) 0%, rgba(236,234,230,0.85) 55%, rgba(236,234,230,0) 100%),
      linear-gradient(180deg, var(--sky-top) 0%, var(--sky-low) 22%, var(--temple-gold) 45%, var(--temple-shade) 100%);
  }
  .headline {
    position: absolute;
    inset: 0;
    width: 1200px;
    height: 676px;
  }
  .headline text {
    font-family: "Noto Sans JP", sans-serif;
    font-weight: 900;
    fill: var(--headline-fill);
    stroke: var(--headline-edge);
    stroke-width: 22px;
    stroke-linejoin: round;
    paint-order: stroke fill;
  }
  .headline .line-one { font-size: 188px; letter-spacing: -6px; }
  .headline .line-two { font-size: 212px; letter-spacing: -4px; }
  .headline .line-three { font-size: 154px; letter-spacing: -4px; }
</style>
</head>
<body>
  <main class="thumbnail">
    <div class="scene-photo" role="img" aria-label="Photo of the host in a white hoodie making peace signs in front of a golden Thai temple under a blue sky"></div>
    <svg class="headline" viewBox="0 0 1200 676" aria-label="バンコクへ戻ってまいりました">
      <text class="line-one" x="8" y="190">バンコクへ</text>
      <text class="line-two" x="18" y="418">戻って</text>
      <text class="line-three" x="14" y="640">まいりました</text>
    </svg>
  </main>
</body>
</html>
```